JesterVolt Balloon Logo and Product Packaging Design

I need a package design for twisting balloons for my website jestervoltfun.com. The brand name that we will use is "jestervolt". The packaging will be 40cm long x 15 cm width with a see thru front and a top that can tear off. We can only use 3 colors max, but two colors would be better. We also will need a logo for "jestervolt". I have included our mockup front and back, our competitors packaging and our style guide. You can use our style guide and our mockups for inspiration but you please don't follow it exactly. You can also ignore them all together. Thanks, Corin

```html
<!DOCTYPE html>
<html lang="en">
<head>
<meta charset="utf-8">
<title>JesterVolt Balloon Packaging</title>
<link rel="stylesheet" href="https://fonts.googleapis.com/css2?family=Archivo+Black&family=Arvo:wght@700&family=Montserrat:wght@500;600&display=swap">
<style>
  :root {
    --board: #ececec;
    --ink: #000000;
    --red: #ee0606;
    --coral: #f25055;
    --yellow: #ffff00;
    --blue: #0587ff;
    --white: #ffffff;
  }
  html, body { margin: 0; padding: 0; overflow: hidden; }
  .canvas {
    position: relative;
    width: 1047px;
    height: 1200px;
    background: var(--board);
    overflow: hidden;
    font-family: "Montserrat", sans-serif;
  }
  .package {
    position: absolute;
    left: 82px;
    top: 85px;
    width: 395px;
    height: 1044px;
    background: var(--white);
    box-shadow: 0 0 0 0.5px #bdbdbd;
  }
  .package-art { position: absolute; inset: 0; display: block; }
  .wordmark {
    position: absolute;
    font-family: "Archivo Black", sans-serif;
    font-weight: 400;
    white-space: nowrap;
    line-height: 1;
    letter-spacing: -0.5px;
  }
  .wordmark--front { left: 0; width: 395px; top: 68px; text-align: center; font-size: 40px; color: var(--ink); }
  .wordmark--footer { left: 212px; top: 992px; font-size: 22px; color: var(--white); }
  .tagline { font-family: "Arvo", serif; font-weight: 700; font-size: 18px; fill: var(--white); }
  .count-number { font-family: "Archivo Black", sans-serif; font-size: 29px; fill: var(--white); }
  .count-unit { font-family: "Archivo Black", sans-serif; font-size: 15px; fill: var(--white); letter-spacing: 1px; }

  .warning {
    position: absolute;
    left: 15px;
    top: 969px;
    width: 171px;
    height: 62px;
    box-sizing: border-box;
    background: var(--white);
    border: 1px solid var(--ink);
    border-radius: 5px;
    padding: 3px 5px;
  }
  .warning-head { display: flex; align-items: center; gap: 4px; }
  .warning-icon { width: 22px; height: 20px; flex: none; }
  .warning-title { font-size: 19px; font-weight: 600; line-height: 1; letter-spacing: -0.3px; }
  .warning-sub { font-size: 11.5px; font-weight: 500; line-height: 1.1; }
  .warning-body { margin-top: 2px; font-size: 4.3px; line-height: 1.3; text-align: center; }

  .swatches { position: absolute; left: 568px; top: 201px; }
  .swatch { position: absolute; top: 0; width: 51px; height: 30px; }
  .swatch--black { left: 0; background: var(--ink); }
  .swatch--red { left: 71px; background: var(--red); }
  .swatch--coral { left: 133px; background: var(--coral); }
  .swatch--yellow { left: 196px; background: var(--yellow); }
  .swatch--blue { left: 257px; background: var(--blue); }
  .swatch--white { left: 325px; background: var(--white); box-shadow: inset 0 0 0 0.5px #c8c8c8; }

  .variant { font-size: 50px; }
  .variant--red { left: 662px; top: 302px; color: var(--red); }
  .variant--black { left: 565px; top: 384px; color: var(--ink); }
  .variant--blue { left: 662px; top: 500px; color: var(--blue); }
  .variant--yellow-blue { left: 565px; top: 602px; color: var(--blue); }
</style>
</head>
<body>
<div class="canvas">

  <section class="package" aria-label="Balloon package front">
    <svg class="package-art" viewBox="0 0 395 1044" width="395" height="1044" aria-hidden="true">
      <!-- header bands -->
      <path fill="var(--blue)" d="M0,0 H395 V199 C360,200 330,180 280,172 C230,165 190,180 140,195 C90,210 40,210 0,196 Z"/>
      <path fill="var(--yellow)" d="M0,54 C70,50 110,10 175,10 C240,10 300,95 395,92 V140 H0 Z"/>
      <path fill="var(--red)" d="M0,72 C80,58 120,40 160,45 C230,52 300,120 395,126 V160 C340,175 290,125 210,135 C120,150 60,175 0,158 Z"/>
      <path id="tagline-arc" fill="none" d="M30,192 C110,148 280,128 372,188"/>
      <text class="tagline"><textPath href="#tagline-arc" startOffset="50%" text-anchor="middle">High-Quality Party Balloons</textPath></text>

      <!-- footer bands -->
      <path fill="var(--red)" d="M0,889 C60,880 120,905 190,955 V1044 H0 Z"/>
      <g class="count-badge">
        <circle cx="198" cy="900" r="64" fill="var(--blue)"/>
        <circle cx="198" cy="900" r="66" fill="none" stroke="var(--blue)" stroke-width="10" stroke-dasharray="8 9"/>
        <text class="count-number" x="198" y="918" text-anchor="middle">100</text>
        <text class="count-unit" x="198" y="935" text-anchor="middle">PCS</text>
      </g>
      <path fill="var(--yellow)" d="M0,914 C70,918 130,940 175,958 C240,935 320,900 395,905 V1044 H0 Z"/>
      <path fill="var(--blue)" d="M0,924 C70,930 120,955 175,967 C250,940 320,920 395,926 V1044 H0 Z"/>
    </svg>

    <div class="wordmark wordmark--front">JesterVolt</div>

    <div class="warning">
      <div class="warning-head">
        <svg class="warning-icon" viewBox="0 0 22 20" aria-hidden="true">
          <path d="M11,1.5 L20.5,18.5 H1.5 Z" fill="none" stroke="var(--red)" stroke-width="1.6" stroke-linejoin="round"/>
          <path d="M11,4.5 L18,17 H4 Z" fill="var(--red)"/>
          <rect x="10.2" y="8" width="1.6" height="5.2" fill="var(--white)"/>
          <rect x="10.2" y="14" width="1.6" height="1.6" fill="var(--white)"/>
        </svg>
        <div>
          <div class="warning-title">WARNING!</div>
          <div class="warning-sub">CHOKING HAZARD</div>
        </div>
      </div>
      <p class="warning-body" style="margin-bottom:0">Children under eight(8) years old can choke or suffocate on uninflated or broken ballons. Adult supervision is required. Keep uninflated ballons from reach of children. Discard broken ballons responsibly.</p>
    </div>

    <div class="wordmark wordmark--footer">JesterVolt</div>
  </section>

  <div class="swatches" aria-label="Colour palette">
    <div class="swatch swatch--black"></div>
    <div class="swatch swatch--red"></div>
    <div class="swatch swatch--coral"></div>
    <div class="swatch swatch--yellow"></div>
    <div class="swatch swatch--blue"></div>
    <div class="swatch swatch--white"></div>
  </div>

  <div class="wordmark variant variant--red">JesterVolt</div>
  <div class="wordmark variant variant--black">JesterVolt</div>
  <div class="wordmark variant variant--blue">JesterVolt</div>
  <div class="wordmark variant variant--yellow-blue">JesterVolt</div>

</div>
</body>
</html>
```